A 3d printing services company "The Velvet Lattice" needs a clutter breaking business card design

The Velvet Lattice is a 3d design, animation and printing services company. We are in the B2B and B2C space. www.velvetlattice.com.sg
We have been in business for a year.
The logo is already done (the current file is attached).
We need a business card design which reflects the 3d printing and animations services of the company. A standard rectangular shape is not an option. The card can be die cut.
The card should have the colors of the logo and should have a high tech wow feel to it.
The front of the card should have my name, designation, cellphone email and website details. No need for an office address.
Name: Raghavan Kulkarni
Designation: Founder Director
Cellphone (65)91827345
email: raghavan@velvetlattice.com.sg
website: www.velvetlattice.com.sg
The back of the card should have the services we offer:
1. 3d Design and Modelling
2. 3d Animation
3. 3D Printing
The tag line is: "make your ideas real"
Am uploading the current business card files(back and front).
Target Market(s)
Business owners and C level managers in Marine, Healthcare industry
Industry/Entity Type
Printing
Contact Information for Business Card
Name: Raghavan Kulkarni
Cellphone (65)91827345
2. 3d Animation
3. 3D Printing

```html
<!DOCTYPE html>
<html lang="en">
<head>
<meta charset="utf-8">
<title>The Velvet Lattice – Business Card</title>
<link href="https://fonts.googleapis.com/css2?family=Roboto+Condensed:wght@700&family=Source+Sans+3:wght@400;600;700&display=swap" rel="stylesheet">
<style>
  :root {
    --paper: #ffffff;
    --ink: #111111;
    --frame: #000000;
    --service-grey: #6d6e71;
    --brand-blue: #1f6fc2;
    --brand-green: #6cc24a;
  }
  * { margin: 0; padding: 0; box-sizing: border-box; }
  html, body {
    width: 1200px;
    height: 696px;
    overflow: hidden;
    background: var(--paper);
  }
  .card {
    position: relative;
    width: 1200px;
    height: 696px;
  }
  .card-shape {
    position: absolute;
    left: 0;
    top: 0;
  }
  .brand-name {
    position: absolute;
    left: 73px;
    top: 150px;
    display: flex;
    align-items: center;
    gap: 14px;
    font-family: "Source Sans 3", sans-serif;
    font-weight: 700;
    font-size: 46px;
    line-height: 1;
    color: var(--brand-blue);
  }
  .brand-dot {
    width: 28px;
    height: 28px;
    border-radius: 50%;
    background: var(--brand-green);
    flex: none;
  }
  .tagline {
    position: absolute;
    left: 115px;
    top: 210px;
    font-family: "Source Sans 3", sans-serif;
    font-weight: 600;
    font-size: 24px;
    letter-spacing: 0.08em;
    color: var(--brand-green);
  }
  .service-list {
    position: absolute;
    left: 106px;
    top: 352px;
    list-style: none;
    font-family: "Source Sans 3", sans-serif;
    font-weight: 400;
    font-size: 37px;
    line-height: 54.5px;
    color: var(--service-grey);
  }
  .contact {
    position: absolute;
    left: 690px;
    top: 300px;
    font-family: "Source Sans 3", sans-serif;
    color: var(--service-grey);
  }
  .contact-name {
    font-weight: 700;
    font-size: 40px;
    line-height: 1.1;
    color: var(--ink);
  }
  .contact-role {
    font-weight: 600;
    font-size: 24px;
    color: var(--brand-blue);
    margin-bottom: 22px;
  }
  .contact-line {
    display: flex;
    align-items: center;
    gap: 12px;
    font-size: 26px;
    line-height: 42px;
  }
  .contact-icon { flex: none; }
  .website {
    position: absolute;
    left: 73px;
    top: 548px;
    font-family: "Roboto Condensed", sans-serif;
    font-weight: 700;
    font-size: 54px;
    letter-spacing: 0.12em;
    color: var(--ink);
  }
</style>
</head>
<body>
  <main class="card">
    <svg class="card-shape" width="1200" height="696" viewBox="0 0 1200 696" aria-hidden="true">
      <defs>
        <linearGradient id="accent" x1="0" y1="0" x2="1" y2="1">
          <stop offset="0" stop-color="var(--brand-green)"/>
          <stop offset="1" stop-color="var(--brand-blue)"/>
        </linearGradient>
      </defs>
      <path d="M10 10 H1090 L1190 110 V686 H90 L10 606 Z" fill="var(--paper)" stroke="var(--frame)" stroke-width="3"/>
      <g fill="none" stroke="url(#accent)">
        <path d="M1010 10 L1190 190" stroke-width="5"/>
        <path d="M960 10 L1190 240" stroke-width="2"/>
        <path d="M10 526 L170 686" stroke-width="2"/>
        <path d="M655 300 V500" stroke-width="5"/>
      </g>
      <g stroke="var(--ink)" stroke-width="3" fill="none">
        <path d="M74 272 V483 H94"/>
        <path d="M74 375 H94"/>
        <path d="M74 429 H94"/>
      </g>
      <g fill="var(--ink)">
        <circle cx="97" cy="375" r="4"/>
        <circle cx="97" cy="429" r="4"/>
        <circle cx="97" cy="483" r="4"/>
      </g>
    </svg>

    <div class="brand-name"><span class="brand-dot"></span>The Velvet Lattice</div>
    <p class="tagline">make your ideas real</p>

    <ul class="service-list">
      <li>Design and Modelling</li>
      <li>Animation</li>
      <li>Printing</li>
    </ul>

    <div class="contact">
      <p class="contact-name">Raghavan Kulkarni</p>
      <p class="contact-role">Founder Director</p>
      <p class="contact-line">
        <svg class="contact-icon" width="22" height="22" viewBox="0 0 24 24" aria-hidden="true"><path d="M6.6 10.8a15.1 15.1 0 0 0 6.6 6.6l2.2-2.2a1 1 0 0 1 1-.25 11.4 11.4 0 0 0 3.6.57 1 1 0 0 1 1 1V20a1 1 0 0 1-1 1A17 17 0 0 1 3 4a1 1 0 0 1 1-1h3.5a1 1 0 0 1 1 1c0 1.25.2 2.45.57 3.57a1 1 0 0 1-.25 1z" fill="var(--brand-blue)"/></svg>
        (65)91827345
      </p>
      <p class="contact-line">
        <svg class="contact-icon" width="22" height="22" viewBox="0 0 24 24" aria-hidden="true"><rect x="2" y="5" width="20" height="14" rx="2" fill="none" stroke="var(--brand-blue)" stroke-width="2"/><path d="M3 6l9 7 9-7" fill="none" stroke="var(--brand-blue)" stroke-width="2"/></svg>
        raghavan@velvetlattice.com.sg
      </p>
    </div>

    <p class="website">www.velvetlattice.com.sg</p>
  </main>
</body>
</html>
```